Poly Bag Packaging Motorcycle Cables - Vorenza Brand

Poly Bag Dimensions: 33cm(H) x 24cm(W)
We would like to design a genuine Poly Bag Packaging for motorcycle cables.
Vorenza, is one of the leading companies for manufacturing Motorcycles, located in Egypt. Our company is offering high-quality products, the best in the local market, with very competitive prices.
We have a limited time to get this project done, So we Highly appreciate receiving your designs ASAP.
Target Market(s)
Motorcycle Spare parts Buyers
Colors
Designer to choose colors to be used in the design.
Look and feel

```html
<!DOCTYPE html>
<html lang="en">
<head>
<meta charset="utf-8">
<title>Vorenza Racing Cable – Poly Bag</title>
<link rel="stylesheet" href="https://fonts.googleapis.com/css2?family=Exo+2:ital,wght@0,800;1,800;1,900&display=swap">
<style>
  :root {
    --yellow: #fdcf07;
    --yellow-soft: #fde27a;
    --black: #000000;
    --white: #ffffff;
    --edge: #d9d9d9;
  }
  * { margin: 0; padding: 0; box-sizing: border-box; }
  html, body {
    width: 1200px;
    height: 1200px;
    overflow: hidden;
    background: var(--white);
  }
  .canvas {
    position: relative;
    width: 1200px;
    height: 1200px;
    background: var(--white);
    font-family: "Exo 2", sans-serif;
  }
  .poly-bag {
    position: absolute;
    left: 298px;
    top: 155px;
    width: 642px;
    height: 883px;
    background: var(--white);
    border: 1px solid var(--edge);
    overflow: hidden;
  }
  .top-band {
    position: absolute;
    left: 0; top: 0;
    width: 100%;
    height: 100px;
    background: var(--yellow);
  }
  .top-stripe {
    position: absolute;
    left: 0; top: 100px;
    width: 100%;
    height: 20px;
    background: var(--black);
  }
  .headline {
    position: absolute;
    left: 0;
    width: 100%;
    text-align: center;
    color: var(--black);
    font-style: italic;
    font-weight: 900;
    letter-spacing: 2px;
    text-transform: uppercase;
    line-height: 1;
  }
  .headline--top { top: 46px; font-size: 40px; padding-left: 18px; }
  .headline--product { top: 132px; font-size: 44px; }
  .flame-art {
    position: absolute;
    left: 62px;
    top: 170px;
    width: 526px;
    height: 620px;
    border-radius: 260px 260px 0 0;
    background: linear-gradient(180deg, var(--yellow-soft) 0%, var(--yellow) 55%);
  }
  .brand-mark {
    position: absolute;
    left: 0;
    top: 470px;
    width: 100%;
    display: flex;
    align-items: center;
    justify-content: center;
    gap: 14px;
  }
  .brand-mark__dot {
    width: 34px;
    height: 34px;
    border-radius: 50%;
    background: var(--black);
  }
  .brand-mark__name {
    font-weight: 800;
    font-style: normal;
    font-size: 50px;
    color: var(--black);
    letter-spacing: 2px;
  }
  .product-label {
    position: absolute;
    left: 0;
    top: 700px;
    width: 100%;
    text-align: center;
    color: var(--black);
    font-style: italic;
    font-weight: 900;
    text-transform: uppercase;
    line-height: 1;
  }
  .product-label__line1 { font-size: 20px; letter-spacing: 1px; }
  .product-label__line2 { font-size: 28px; letter-spacing: 2px; margin-top: 4px; }
  .bottom-band {
    position: absolute;
    left: 0; top: 782px;
    width: 100%;
    height: 78px;
    background: var(--yellow);
  }
  .bottom-stripe {
    position: absolute;
    left: 0; top: 860px;
    width: 100%;
    height: 20px;
    background: var(--black);
  }
  .bottom-edge {
    position: absolute;
    left: 0; top: 880px;
    width: 100%;
    height: 3px;
    background: var(--yellow);
  }
</style>
</head>
<body>
<div class="canvas">
  <div class="poly-bag">
    <div class="top-band"></div>
    <div class="top-stripe"></div>
    <h1 class="headline headline--top">High Performance</h1>
    <h2 class="headline headline--product">Racing Cable</h2>

    <div class="flame-art" role="img" aria-label="Yellow flame illustration rising behind the brand"></div>

    <div class="brand-mark">
      <span class="brand-mark__dot"></span>
      <span class="brand-mark__name">Vorenza</span>
    </div>

    <div class="product-label">
      <div class="product-label__line1">Performance</div>
      <div class="product-label__line2">Break Cable</div>
    </div>

    <div class="bottom-band"></div>
    <div class="bottom-stripe"></div>
    <div class="bottom-edge"></div>
  </div>
</div>
</body>
</html>
```